Kitchen and Bathroom Remodeling Flyer

This flyer is for a home remodeling company that remodels peoples kitchens and bathrooms.

We want a flyer to be sophisticated: nice professional design with classy font.

FRONT OF FLYER:

I have attached the front flyer I created and there is no design to it. The reason is so you can see what text elements we want on the flyer. a second attachment has the text for easy copy and paste.

I like the idea of mentioning “Owners live in Ahwatukee” because this flyer will be passed around door to door in that town of Ahwatukee.

Please use the image and the corresponding headline specific to that image. The headline can be in the image or to the top of the image.

BACK OF FLYER:
The back of flyer is essentially a written letter with a profile image of our owners and then two testimonials at bottom. I’d like to add a little bit of design to the back of the flyer. See attachment for pdf of current text and basic structure.

Our brand colors are gray and blue# 0000cc

Our website is https://Kelmbrookrenovating.com

Thank you,
Tobias

Target Market(s)

Mostly woman. Homeowners making 100k+ a year that want to remodel their kitchen or bathroom

Industry/Entity Type

Home Improvement

Font styles to use
Serif
Sans Serif
Decorative

Colors

Designer to choose colors to be used in the design.

Requirements
Must have
• This has to be in photoshop with each element editable (I’ll want to change things down the road)
Nice to have
• Examples that I don’t want copied but so you have a rough idea of some design structure that I like:
• https://flyer.pixelvantyard.com/contest.aspx?id=5190362
• https://flyer.pixelvantyard.com/contest.aspx?id=627053
• https://flyer.pixelvantyard.com/contest.aspx?id=8831475
• https://www.pixelvantyard.com/design/42957018
• https://www.pixelvantyard.com/design/7160243
Should not have
• Nothing silly or too loud. Thank you

```html
<!DOCTYPE html>
<html lang="en">
<head>
<meta charset="utf-8">
<title>Kelmbrook Renovating – Ahwatukee Flyer</title>
<link rel="stylesheet" href="https://fonts.googleapis.com/css2?family=Josefin+Sans:wght@300;400;600&family=PT+Sans:ital,wght@0,400;0,700;1,400;1,700&display=swap">
<style>
  :root {
    --navy: #243a5a;
    --gray: #8c939c;
    --paper: #ffffff;
    --stage: #e4e4e4;
    --ink-soft: #4a5a72;
    --pale: #dfe4ea;
  }
  * { box-sizing: border-box; margin: 0; padding: 0; }
  html, body { width: 1200px; height: 1200px; overflow: hidden; background: var(--stage); }
  body { position: relative; font-family: "PT Sans", sans-serif; color: var(--navy); }

  .page { position: absolute; top: 247px; width: 500px; height: 705px; background: var(--paper); overflow: hidden; }
  .page--back { left: 60px; }
  .page--front { left: 640px; }
  .block { position: absolute; }

  /* Back page */
  .top-strip { top: 0; left: 0; width: 100%; height: 12px; background: var(--gray); }
  .top-strip::before { content: ""; position: absolute; left: 0; top: 0; width: 150px; height: 100%; background: var(--navy); }
  .letter { top: 32px; left: 32px; right: 38px; }
  .letter__greeting { font-weight: 700; font-style: italic; font-size: 17px; margin-bottom: 8px; }
  .letter p { font-style: italic; font-size: 8.6px; line-height: 1.55; color: var(--ink-soft); margin-bottom: 10px; }
  .letter .letter__signoff { font-weight: 700; color: var(--navy); }

  .owners-band { top: 320px; left: 0; width: 100%; height: 129px; background: var(--gray); }
  .owners-band__photo { position: absolute; left: 40px; top: 10px; width: 90px; height: 110px; }
  .owners-band__info { position: absolute; left: 145px; top: 38px; font-size: 9px; line-height: 1.4; color: var(--paper); }
  .owners-band__info strong { font-style: italic; }

  .testimonial { top: 457px; height: 177px; background: var(--navy); color: var(--paper); }
  .testimonial--one { left: 0; width: 249px; }
  .testimonial--two { left: 255px; width: 245px; }
  .testimonial__photo { position: absolute; left: 20px; top: 20px; width: 72px; height: 72px; }
  .testimonial__name { position: absolute; left: 20px; top: 100px; font-size: 9px; }
  .testimonial__place { position: absolute; left: 20px; top: 114px; font-size: 7px; font-style: italic; color: var(--pale); }
  .testimonial__quote { position: absolute; left: 112px; top: 68px; right: 12px; font-size: 7.5px; line-height: 1.4; }
  .testimonial__quote p + p { margin-top: 8px; }

  .back-footer__site { top: 664px; left: 18px; font-size: 12px; color: var(--ink-soft); }

  /* Brand name lockup */
  .brand { display: flex; align-items: center; gap: 6px; font-family: "PT Sans", sans-serif; font-size: 12px; font-weight: 400; color: var(--navy); }
  .brand__mark { width: 9px; height: 9px; background: var(--navy); }
  .brand--back { top: 658px; right: 20px; }
  .brand--front { top: 660px; right: 22px; }

  /* Front page */
  .headline-panel { top: 0; left: 0; width: 100%; height: 174px; background: var(--navy); color: var(--paper); font-family: "Josefin Sans", sans-serif; }
  .headline-panel__small { position: absolute; left: 36px; top: 36px; font-size: 30px; font-weight: 400; line-height: 1.05; letter-spacing: 0.5px; }
  .headline-panel__town { position: absolute; left: 34px; top: 103px; font-size: 54px; font-weight: 400; letter-spacing: 1px; }

  .feature-caption { top: 174px; height: 92px; font-family: "Josefin Sans", sans-serif; font-weight: 300; text-transform: uppercase; }
  .feature-caption small { display: block; font-size: 9px; line-height: 1.15; }
  .feature-caption span { display: block; font-size: 17px; font-weight: 400; margin-top: 2px; }
  .feature-caption--bath { left: 0; width: 196px; padding: 28px 0 0 14px; color: var(--navy); background: var(--paper); }
  .feature-caption--kitchen { left: 196px; width: 304px; padding: 28px 0 0 28px; color: var(--paper); background: var(--gray); }

  .feature-photo { top: 266px; height: 162px; }
  .feature-photo--bath { left: 0; width: 187px; background: linear-gradient(180deg, #b9b4ad 0%, #7d7168 55%, #d8d4cf 100%); }
  .feature-photo--kitchen { left: 196px; width: 304px; background: linear-gradient(180deg, #cfcdca 0%, #eeeeec 45%, #a9aaab 100%); }

  .call-panel { top: 437px; left: 0; width: 187px; height: 190px; background: var(--gray); color: var(--paper); text-align: center; font-family: "Josefin Sans", sans-serif; padding-top: 70px; }
  .call-panel__label { font-size: 17px; }
  .call-panel__phone { font-size: 22px; line-height: 1; }
  .call-panel__note { font-size: 10px; text-transform: uppercase; }

  .promises { top: 437px; left: 196px; width: 304px; height: 190px; background: var(--navy); color: var(--paper); padding: 20px 20px 0 20px; }
  .promises h2 { font-size: 11px; font-weight: 700; font-style: italic; text-transform: uppercase; margin-bottom: 10px; }
  .promises ul { list-style: none; }
  .promises li { font-size: 8.6px; line-height: 1; margin-bottom: 13px; }
  .promises li::before { content: "•"; margin-right: 4px; }

  .front-footer { top: 646px; left: 12px; font-size: 8.5px; line-height: 1.3; color: var(--navy); }
</style>
</head>
<body>

<section class="page page--back" aria-label="Flyer back">
  <div class="block top-strip"></div>

  <article class="block letter">
    <h1 class="letter__greeting">Dear Ahwatukee Homeowners,</h1>
    <p>Everyone wants a dream home they can be proud of. We all want to feel prosperous in life and our home is an extension of ourselves, our style and feeling successful.</p>
    <p>We understand working with a remodeling contractor can be frustrating because they show up late, change the price and make a mess of your home.</p>
    <p>Kelmbrook Renovating is the most organized remodeling company in the valley and we'll create the dream space you'll be proud to show off to your friends, family, &amp; neighbors.</p>
    <p>One of our co-founders Tobias has been through several contractor nightmares and it is the main reason Tobias, Silas and Wendell founded Kelmbrook Renovating.</p>
    <p>We are an award-winning home remodeling licensed contractor that is known for showing up on time, being organized, clearly explaining all aspects of the remodel, adhering to project budget and timeline.</p>
    <p>One of our client's said we were the AutoNest of home remodeling and we think that's a nice comparison. We'll guide you through our 4 step process and there's no haggle, no sales BS and our clients love the experience.</p>
    <p class="letter__signoff">To a beautiful home you'll love showing off to your neighbors, family &amp; friends,</p>
  </article>

  <div class="block owners-band">
    <div class="owners-band__photo" role="img" aria-label="Portrait of the company co-founder" style="background: linear-gradient(180deg, #1c1c1c 0%, #3a3a3a 60%, #1f6fc0 100%);"></div>
    <div class="owners-band__info">
      <strong>Tobias, Wendell and Silas</strong><br>
      Kelmbrook Renovating<br>
      ROC# 527104<br>
      Kelmbrookrenovating.com<br>
      480-555-0143
    </div>
  </div>

  <div class="block testimonial testimonial--one">
    <div class="testimonial__photo" role="img" aria-label="Photo of a happy client couple" style="background: linear-gradient(180deg, #a8b3b8 0%, #c9b59c 60%, #5f8d5a 100%);"></div>
    <div class="testimonial__name">Owen and Lia P.</div>
    <div class="testimonial__place">Biltmore, Phoenix, AZ</div>
    <div class="testimonial__quote">
      <p>"Our bathroom is amazing! The crew was polite, easy to work with and they kept our house clean.</p>
      <p>I always knew what was happening and there weren't any surprises. My wife and I are very happy. Thank you!"</p>
    </div>
  </div>

  <div class="block testimonial testimonial--two">
    <div class="testimonial__photo" role="img" aria-label="Photo of a smiling client couple" style="background: linear-gradient(180deg, #c7b6a0 0%, #6b5a4c 50%, #2a2a2e 100%);"></div>
    <div class="testimonial__name">Marisa &amp; Joel T.</div>
    <div class="testimonial__place">Chandler, AZ</div>
    <div class="testimonial__quote">
      <p>"Wendell and his team were easy to work with and their attention to detail was great.</p>
      <p>Our kitchen looks perfect just how we wanted it and we couldn't be happier. Thank you Kelmbrook Renovating."</p>
    </div>
  </div>

  <div class="block back-footer__site">Kelmbrookrenovating.com</div>
  <div class="block brand brand--back"><span class="brand__mark"></span>Kelmbrook Renovating</div>
</section>

<section class="page page--front" aria-label="Flyer front">
  <header class="block headline-panel">
    <div class="headline-panel__small">OWNERS<br>LIVE-IN</div>
    <div class="headline-panel__town">AHWATUKEE</div>
  </header>

  <div class="block feature-caption feature-caption--bath">
    <small>Turn an<br>old bathroom into your own</small>
    <span>Personal Spa</span>
  </div>
  <div class="block feature-caption feature-caption--kitchen">
    <small>Entertain in a kitchen<br>you'll love showing off to</small>
    <span>Friends &amp; Family</span>
  </div>

  <div class="block feature-photo feature-photo--bath" role="img" aria-label="Remodeled bathroom with double vanity and freestanding tub"></div>
  <div class="block feature-photo feature-photo--kitchen" role="img" aria-label="Bright white remodeled kitchen with large island"></div>

  <div class="block call-panel">
    <div class="call-panel__label">CALL</div>
    <div class="call-panel__phone">480-555-0143</div>
    <div class="call-panel__note">For more information</div>
  </div>

  <div class="block promises">
    <h2>Our Client Promises:</h2>
    <ul>
      <li>Provide honest and straight forward advice</li>
      <li>Return calls and show up on time</li>
      <li>Employ professional, respectful and knowledgeable employees</li>
      <li>Respect your home and ensure we keep it clean</li>
      <li>Provide clear expectations of project timelines and pricing</li>
      <li>Create your dream living space with great attention to detail</li>
    </ul>
  </div>

  <div class="block front-footer">
    Kelmbrook Renovating<br>
    480-555-0143 ROC# 527104<br>
    Kelmbrookrenovating.com<br>
    LICENSED | BONDED | INSURED
  </div>
  <div class="block brand brand--front"><span class="brand__mark"></span>Kelmbrook Renovating</div>
</section>

</body>
</html>
```